RTB sticker for the back window of a car

Well this design is for the back of our car. We want it to be plain and simple but stand out. I have put something together which is a bit to plain and i would like to to look a little bit different. Possibly have a picture of a shipping container on it so people know what we are trying to sell? I don't need our logo on there but i want the phone number and email. Thank you in advance.

Requirements
Must have
• The phone number 0462 517 093 not the one in the picture please.
• Also must have the email that IS in the picture please.
Nice to have
• A picture of a shipping container so people know what we are talking about.

```html
<!DOCTYPE html>
<html lang="en">
<head>
<meta charset="utf-8">
<title>RTB – Shipping Containers for Sale window sticker</title>
<link rel="stylesheet" href="https://fonts.googleapis.com/css2?family=Roboto+Condensed:wght@700&family=Archivo+Black&display=swap">
<style>
  :root {
    --page-bg: #e9e9e7;
    --sticker-black: #000000;
    --sticker-white: #ffffff;
    --container-light: #f4f4f4;
    --container-shade: #cfcfcf;
  }
  html, body {
    margin: 0;
    padding: 0;
    width: 1200px;
    height: 999px;
    overflow: hidden;
    background: var(--page-bg);
  }
  .canvas {
    position: relative;
    width: 1200px;
    height: 999px;
  }
  .sticker-shape {
    position: absolute;
    left: 0;
    top: 0;
  }
  .headline,
  .headline-for,
  .phone,
  .email {
    position: absolute;
    margin: 0;
    color: var(--sticker-white);
    font-family: "Roboto Condensed", "Arial Narrow", sans-serif;
    font-weight: 700;
    line-height: 1;
    white-space: nowrap;
  }
  .headline {
    left: 213px;
    top: 233px;
    font-size: 59px;
    letter-spacing: -0.3px;
  }
  .headline-for {
    left: 252px;
    top: 336px;
    font-size: 58px;
  }
  .headline-sale {
    position: absolute;
    left: 333px;
    top: 292px;
    margin: 0;
    color: var(--sticker-white);
    font-family: "Archivo Black", "Arial Black", sans-serif;
    font-size: 106px;
    line-height: 1;
    letter-spacing: -1px;
  }
  .phone {
    left: 647px;
    top: 391px;
    font-size: 49px;
  }
  .email {
    left: 650px;
    top: 446px;
    font-size: 27px;
  }
  .container-art {
    position: absolute;
    left: 722px;
    top: 250px;
    width: 278px;
    height: 96px;
    background: linear-gradient(90deg, var(--container-light) 0%, var(--container-light) 30%, var(--container-shade) 100%);
  }
</style>
</head>
<body>
  <main class="canvas">
    <svg class="sticker-shape" width="1200" height="999" viewBox="0 0 1200 999" aria-hidden="true">
      <path fill="var(--sticker-black)"
        d="M228 196 H952 Q990 196 1000 232 L1052 440 Q1062 488 1020 498 Q590 548 160 498 Q118 490 128 442 L180 232 Q190 196 228 196 Z"/>
    </svg>

    <h1 class="headline">Shipping Containers</h1>
    <p class="headline-for">for</p>
    <p class="headline-sale">SALE</p>

    <div class="container-art" role="img" aria-label="Simple white illustration of a shipping container"></div>

    <p class="phone">Ph: 0462 517 093</p>
    <p class="email">Email: sales@rtbunits.com.au</p>
  </main>
</body>
</html>
```